Royal Meadow Hamper company needs a brochure design

We need a brochure design for a new company in Dubai called 'Royal Meadow Hampers'. We already have a logo designed which I have attached and would like to use this and the green/gold/white colours for our brochure. Our company initially will be supplying Royal Meadow Hamper wear of traditional wicker baskets in many designs which hold all the cutlery, crockery and accessories. We will also be selling picnic accessories. We want to purvey a sense of luxury and class in line with our logo. I have attached some photos of the picnicwear. As our products are changing all the time I thought a fold out cover which stays the same and then product cards inserted into the folder which can be changed according to our product changes. I am looking for a fairly simple design and each product card should have at least one photo of the product on it with a spec and description also. On the cover of the folder I would like room to write about the company and what we do, this can be inside or out and may or may not include photos. I have the logo designs in illustrator format and pdf. Please contact if any more information is needed.

Reason: I have extended this deadline as there are some content changes taking place.

```html
<!DOCTYPE html>
<html lang="en">
<head>
<meta charset="utf-8">
<title>Royal Meadow Hampers – Brochure</title>
<link href="https://fonts.googleapis.com/css2?family=Lato:wght@400;700;900&display=swap" rel="stylesheet">
<style>
  :root {
    --green-deep: #173d14;
    --green: #2b5e1c;
    --green-light: #4a8a2a;
    --gold: #d9a514;
    --gold-light: #f0c43a;
    --white: #ffffff;
    --ink: #2a2a2a;
    --page: #e9e9e6;
    --wicker: #c99a5b;
    --wicker-light: #ecdcc0;
  }
  * { box-sizing: border-box; margin: 0; padding: 0; }
  html, body { width: 1200px; height: 1200px; overflow: hidden; }
  body { background: var(--page); font-family: "Lato", sans-serif; position: relative; color: var(--ink); }

  .piece { position: absolute; background: var(--white); overflow: hidden; box-shadow: 0 4px 14px rgba(0,0,0,.18); }
  .piece > svg.shapes { position: absolute; inset: 0; }
  .abs { position: absolute; }

  .brand-name {
    font-family: "Lato", sans-serif; font-weight: 700; color: var(--gold);
    text-transform: uppercase; letter-spacing: .22em; white-space: nowrap;
    display: flex; align-items: center; gap: 8px;
  }
  .brand-name .mark { width: 8px; height: 8px; border-radius: 50%; background: var(--gold); }

  .photo { background: radial-gradient(ellipse at 50% 45%, var(--wicker-light) 0%, var(--wicker) 70%, #9c6f38 100%); border-radius: 4px; }

  .product-title { font-weight: 900; color: var(--gold); text-transform: uppercase; letter-spacing: -.01em; text-align: center; }
  .product-desc { color: var(--white); text-align: center; }

  .contact { color: var(--white); font-weight: 700; display: flex; align-items: center; gap: 8px; white-space: nowrap; }
  .contact svg { flex: none; }

  /* open spread */
  .spread { left: 40px; top: 40px; width: 1120px; height: 500px; }
  .spread .spine { position: absolute; left: 559px; top: 0; width: 2px; height: 100%; background: rgba(0,0,0,.06); }
  .overview-heading {
    left: 26px; top: 64px; background: var(--green-deep); color: var(--white);
    font-weight: 700; font-size: 22px; padding: 6px 22px 8px 14px; border-radius: 0 18px 18px 0;
  }
  .spec-list { left: 34px; top: 116px; list-style: none; font-size: 12.5px; line-height: 18px; }
  .spec-list li { display: flex; align-items: center; gap: 8px; }
  .spec-list li::before { content: ""; width: 7px; height: 7px; background: var(--gold); border-radius: 50%; flex: none; }
  .spread .side-photo { left: 28px; top: 382px; width: 150px; height: 104px; }
  .contact-name { left: 300px; top: 402px; background: var(--green-deep); border-radius: 14px; padding: 7px 14px; font-size: 10px; }
  .spread .phone { left: 306px; top: 438px; font-size: 20px; }
  .spread .web { left: 306px; top: 470px; font-size: 12px; }
  .spread .logo-top { left: 560px; width: 560px; top: 34px; justify-content: center; font-size: 15px; }
  .spread .main-photo { left: 650px; top: 122px; width: 380px; height: 150px; }
  .spread .product-title { left: 560px; width: 560px; top: 350px; font-size: 40px; }
  .spread .product-desc { left: 620px; width: 440px; top: 406px; font-size: 10.5px; line-height: 14px; }

  /* product card */
  .card { left: 800px; top: 600px; width: 360px; height: 540px; }
  .card .logo-top { left: 0; width: 360px; top: 36px; justify-content: center; font-size: 13px; }
  .card .main-photo { left: 30px; top: 150px; width: 300px; height: 180px; }
  .card .product-title { left: 0; width: 360px; top: 386px; font-size: 36px; }
  .card .product-desc { left: 24px; width: 312px; top: 436px; font-size: 9.5px; line-height: 12.5px; }

  /* folder inside */
  .folder { left: 40px; top: 600px; width: 720px; height: 540px; }
  .folder .spine { position: absolute; left: 359px; top: 0; width: 2px; height: 100%; background: rgba(0,0,0,.06); }
  .folder .logo-top { left: 360px; width: 360px; top: 36px; justify-content: center; font-size: 12px; }
  .about { left: 388px; top: 140px; width: 306px; font-size: 12px; line-height: 16px; color: var(--ink); }
  .about p + p { margin-top: 8px; }

  .insert { left: 14px; top: 318px; width: 330px; height: 200px; box-shadow: 0 3px 10px rgba(0,0,0,.25); }
  .insert .logo-top { left: 0; width: 330px; top: 12px; justify-content: center; font-size: 8px; }
  .insert .main-photo { left: 10px; top: 52px; width: 130px; height: 136px; }
  .insert .insert-title { left: 150px; width: 172px; top: 56px; font-size: 22px; font-weight: 900; color: var(--green); text-align: center; text-transform: uppercase; }
  .insert .insert-desc { left: 152px; width: 170px; top: 86px; font-size: 7px; line-height: 9px; color: var(--ink); }
  .insert .phone { right: 10px; top: 168px; font-size: 11px; gap: 5px; }
  .insert .web { right: 10px; top: 186px; font-size: 7px; }
</style>
</head>
<body>

<section class="piece spread">
  <svg class="shapes" width="1120" height="500" viewBox="0 0 1120 500" aria-hidden="true">
    <defs>
      <linearGradient id="greenA" x1="0" y1="0" x2="1" y2="1">
        <stop offset="0" stop-color="#173d14"/><stop offset=".6" stop-color="#2b5e1c"/><stop offset="1" stop-color="#4a8a2a"/>
      </linearGradient>
    </defs>
    <path d="M0 0 H560 V24 C380 30 180 10 0 48 Z" fill="url(#greenA)"/>
    <path d="M560 0 H1120 V72 C950 100 760 110 560 150 Z" fill="url(#greenA)"/>
    <path d="M560 156 C760 116 950 106 1120 78" fill="none" stroke="#d9a514" stroke-width="4"/>
    <path d="M560 332 C760 320 950 292 1120 262 V500 H560 Z" fill="url(#greenA)"/>
    <path d="M560 324 C760 312 950 284 1120 254" fill="none" stroke="#d9a514" stroke-width="5"/>
    <path d="M120 500 C260 420 420 360 560 300 V500 Z" fill="url(#greenA)"/>
    <path d="M110 500 C250 414 412 352 560 292" fill="none" stroke="#d9a514" stroke-width="4"/>
  </svg>
  <div class="spine"></div>

  <h2 class="abs overview-heading">Picnic basket overview:</h2>
  <ul class="abs spec-list">
    <li>Handmade light full buff willow for four people</li>
    <li>Tan leather straps and trim</li>
    <li>Removable cream cooler bag</li>
    <li>Contemporary cream and white colour palette</li>
    <li>4 white china plates</li>
    <li>4 stainless steel knives, forks and spoons</li>
    <li>1 Stainless steel waiters friend bottle opener</li>
    <li>Stainless steel salt and pepper mills</li>
    <li>1 Stainless steel flask</li>
    <li>4 Cream napkins</li>
    <li>1 wooden chopping board</li>
    <li>4 wine glasses</li>
    <li>4 China mugs held in a willow basket 240 x 240 x 110mm</li>
    <li>Hamper dimensions, 380 x 380 x 210mm</li>
  </ul>
  <div class="abs photo side-photo" role="img" aria-label="Photo of a small open wicker picnic basket"></div>

  <div class="abs brand-name contact-name"><span class="mark"></span>Royal Meadow Hampers</div>
  <div class="abs contact phone">
    <svg width="18" height="18" viewBox="0 0 24 24"><path d="M6.6 10.8a15 15 0 0 0 6.6 6.6l2.2-2.2a1 1 0 0 1 1-.25 11.4 11.4 0 0 0 3.6.6 1 1 0 0 1 1 1V20a1 1 0 0 1-1 1A17 17 0 0 1 3 4a1 1 0 0 1 1-1h3.5a1 1 0 0 1 1 1c0 1.25.2 2.45.6 3.6a1 1 0 0 1-.25 1z" fill="#fff"/></svg>
    000-000-000
  </div>
  <div class="abs contact web">
    <svg width="16" height="12" viewBox="0 0 16 12"><rect x="0.5" y="0.5" width="15" height="11" fill="none" stroke="#fff"/><path d="M0.5 0.5 L8 7 L15.5 0.5" fill="none" stroke="#fff"/></svg>
    www.royalmeadow-hampers.example
  </div>

  <div class="abs brand-name logo-top"><span class="mark"></span>Royal Meadow Hampers</div>
  <div class="abs photo main-photo" role="img" aria-label="Photo of the open Ashford wicker picnic hamper with plates, cutlery and flask"></div>
  <h1 class="abs product-title">The Ashford</h1>
  <p class="abs product-desc">This luxury fitted picnic basket is the epitome of stylish outdoor dining, hand crafted in honey coloured buff willow with tan leather straps and trims it comes equipped for four people. Internally the basket is furnished with beautiful cream fabrics including stylish napkins, a stainless steel flask and ceramic mugs are included to ensure that a perfect cup of tea can be enjoyed outside. Wine glasses are also included to ensure that this is the perfect accessory for a leisurely afternoon tea with family or friends.</p>
</section>

<section class="piece folder">
  <svg class="shapes" width="720" height="540" viewBox="0 0 720 540" aria-hidden="true">
    <defs>
      <linearGradient id="greenB" x1="0" y1="0" x2="1" y2="1">
        <stop offset="0" stop-color="#173d14"/><stop offset=".6" stop-color="#2b5e1c"/><stop offset="1" stop-color="#4a8a2a"/>
      </linearGradient>
    </defs>
    <path d="M0 0 H720 V66 C580 80 460 96 360 124 C240 56 120 30 0 24 Z" fill="url(#greenB)"/>
    <path d="M360 130 C460 102 580 86 720 72" fill="none" stroke="#d9a514" stroke-width="4"/>
    <path d="M40 540 C300 520 560 420 720 326 V540 Z" fill="url(#greenB)"/>
    <path d="M30 540 C290 514 552 412 720 318" fill="none" stroke="#d9a514" stroke-width="5"/>
  </svg>
  <div class="spine"></div>
  <div class="abs brand-name logo-top"><span class="mark"></span>Royal Meadow Hampers</div>
  <div class="abs about">
    <p>Lorem Ipsum is simply dummy text of the printing and typesetting industry. Lorem Ipsum has been the industry's standard dummy text ever since the 1500s, when an unknown printer took a galley of type and scrambled it to make a type specimen book.</p>
    <p>Lorem Ipsum is simply dummy text of the printing and typesetting industry.</p>
    <p>Lorem Ipsum is simply dummy text of the printing and typesetting industry. Lorem Ipsum has been the industry's standard dummy text ever since the 1500s, when an unknown printer took a galley of type and scrambled it to make a type specimen book.</p>
  </div>

  <div class="piece insert">
    <svg class="shapes" width="330" height="200" viewBox="0 0 330 200" aria-hidden="true">
      <path d="M0 0 H330 V30 C220 38 110 34 0 48 Z" fill="url(#greenB)"/>
      <path d="M0 52 C110 38 220 42 330 34" fill="none" stroke="#d9a514" stroke-width="2.5"/>
      <path d="M100 200 C180 185 260 165 330 145 V200 Z" fill="url(#greenB)"/>
      <path d="M86 200 C170 180 252 159 330 138" fill="none" stroke="#d9a514" stroke-width="2.5"/>
    </svg>
    <div class="abs brand-name logo-top"><span class="mark"></span>Royal Meadow Hampers</div>
    <div class="abs photo main-photo" role="img" aria-label="Photo of the open Ashford wicker picnic hamper"></div>
    <h3 class="abs insert-title">The Ashford</h3>
    <p class="abs insert-desc">This luxury fitted picnic basket is the epitome of stylish outdoor dining, hand crafted in honey coloured buff willow with tan leather straps and trims it comes equipped for four people.</p>
    <div class="abs contact phone">
      <svg width="10" height="10" viewBox="0 0 24 24"><path d="M6.6 10.8a15 15 0 0 0 6.6 6.6l2.2-2.2a1 1 0 0 1 1-.25 11.4 11.4 0 0 0 3.6.6 1 1 0 0 1 1 1V20a1 1 0 0 1-1 1A17 17 0 0 1 3 4a1 1 0 0 1 1-1h3.5a1 1 0 0 1 1 1c0 1.25.2 2.45.6 3.6a1 1 0 0 1-.25 1z" fill="#fff"/></svg>
      000-000-000
    </div>
    <div class="abs contact web">www.royalmeadow-hampers.example</div>
  </div>
</section>

<section class="piece card">
  <svg class="shapes" width="360" height="540" viewBox="0 0 360 540" aria-hidden="true">
    <defs>
      <linearGradient id="greenC" x1="0" y1="0" x2="1" y2="1">
        <stop offset="0" stop-color="#173d14"/><stop offset=".6" stop-color="#2b5e1c"/><stop offset="1" stop-color="#4a8a2a"/>
      </linearGradient>
    </defs>
    <path d="M0 0 H360 V128 C240 104 120 96 0 92 Z" fill="url(#greenC)"/>
    <path d="M0 98 C120 102 240 110 360 134" fill="none" stroke="#d9a514" stroke-width="4"/>
    <path d="M0 392 C120 372 240 352 360 332 V540 H0 Z" fill="url(#greenC)"/>
    <path d="M0 384 C120 364 240 344 360 324" fill="none" stroke="#d9a514" stroke-width="5"/>
  </svg>
  <div class="abs brand-name logo-top"><span class="mark"></span>Royal Meadow Hampers</div>
  <div class="abs photo main-photo" role="img" aria-label="Photo of the open Ashford wicker picnic hamper with plates, cutlery and mugs"></div>
  <h2 class="abs product-title">The Ashford</h2>
  <p class="abs product-desc">This luxury fitted picnic basket is the epitome of stylish outdoor dining, hand crafted in honey coloured buff willow with tan leather straps and trims it comes equipped for four people. Internally the basket is furnished with beautiful cream fabrics including stylish napkins, a stainless steel flask and ceramic mugs are included to ensure that a perfect cup of tea can be enjoyed outside. Wine glasses are also included to ensure that this is the perfect accessory for a leisurely afternoon tea with family or friends.</p>
</section>

</body>
</html>
```